Business cards and stationary design

We just completed the design of our new logo and we need to print new business cards and letterhead for our nonprofit. We are looking for a fresh new design that shows off our new logo. On letterhead, we must have a column on the right or left to include our Board of Directors (up to 45 names) (see attachment)

Industry/Entity Type

Non-Profit

Contact Information for Business Card

Standard business card with name, title, Company name, mailing address phone numbers, email address and website. Tagline on back "Bringing the homeless home"

Font styles to use
Sans Serif

Requirements
Must have
• include pertinent information above
• new logo
• fonts compatible with logo
• should use logo colors only
Nice to have
• tag lines

```html
<!DOCTYPE html>
<html lang="en">
<head>
<meta charset="utf-8">
<title>Homeward Haven Center — Business Card</title>
<link href="https://fonts.googleapis.com/css2?family=Michroma&family=Open+Sans:wght@400;600&display=swap" rel="stylesheet">
<style>
  :root {
    --teal: #0f7a94;
    --teal-deep: #0b6980;
    --red: #e0262b;
    --amber: #f0a81e;
    --ink: #2b2b2b;
    --paper: #f7f7f5;
    --stage: #e6e4e0;
    --white: #ffffff;
  }
  * { margin: 0; padding: 0; box-sizing: border-box; }
  html, body {
    width: 1200px; height: 1200px; overflow: hidden;
    background: var(--stage);
  }
  .canvas { position: relative; width: 1200px; height: 1200px; }
  .card {
    position: absolute; left: 150px; width: 900px; height: 515px;
    border-radius: 4px;
    box-shadow: 0 6px 18px rgba(0,0,0,0.18);
    overflow: hidden;
  }
  .card--back {
    top: 70px;
    background: linear-gradient(160deg, var(--teal) 0%, var(--teal-deep) 100%);
    display: flex; align-items: center; justify-content: center;
  }
  .card--front { top: 615px; background: var(--paper); }

  .brand-name {
    display: flex; align-items: center; gap: 12px;
    font-family: "Open Sans", sans-serif;
    font-weight: 600;
    white-space: nowrap;
  }
  .brand-name__dot {
    width: 22px; height: 22px; border-radius: 50%; flex: none;
    background: currentColor;
  }
  .brand-name--back { color: var(--white); font-size: 34px; }
  .brand-name--front { color: var(--teal); font-size: 28px; }

  .front-brand {
    position: absolute; left: 30px; top: 0; width: 440px; height: 100%;
    display: flex; align-items: center; justify-content: center;
  }

  .divider {
    position: absolute; left: 492px; top: 130px; width: 2px; height: 250px;
    background: var(--teal);
  }
  .contact {
    position: absolute; left: 530px; top: 118px; width: 340px;
    font-family: "Open Sans", sans-serif; color: var(--ink);
  }
  .contact__name {
    font-family: "Michroma", sans-serif; color: var(--teal);
    font-size: 23px; letter-spacing: 0.08em; text-transform: uppercase;
  }
  .contact__title {
    font-family: "Michroma", sans-serif; color: var(--red);
    font-size: 13px; letter-spacing: 0.14em; text-transform: uppercase;
    margin-top: 4px;
  }
  .contact__address { font-size: 16px; line-height: 1.55; margin-top: 18px; }
  .contact__list { list-style: none; margin-top: 14px; }
  .contact__item {
    display: flex; align-items: center; gap: 14px;
    font-size: 17px; line-height: 1.75;
  }
  .contact__icon { width: 18px; height: 18px; flex: none; }
</style>
</head>
<body>
<main class="canvas">

  <section class="card card--back" aria-label="Card back">
    <h2 class="brand-name brand-name--back"><span class="brand-name__dot" aria-hidden="true"></span>Homeward Haven Center</h2>
  </section>

  <section class="card card--front" aria-label="Card front">
    <div class="front-brand">
      <h1 class="brand-name brand-name--front"><span class="brand-name__dot" aria-hidden="true"></span>Homeward Haven Center</h1>
    </div>

    <div class="divider"></div>

    <div class="contact">
      <p class="contact__name">Daniel Marsh</p>
      <p class="contact__title">Managing Director</p>
      <p class="contact__address">Level 4, Suite 12, 88 Harbour Street<br>Riverside, Victoria 3000</p>
      <ul class="contact__list">
        <li class="contact__item">
          <svg class="contact__icon" viewBox="0 0 24 24" aria-hidden="true"><path fill="var(--amber)" d="M6.6 10.8a15.1 15.1 0 0 0 6.6 6.6l2.2-2.2a1 1 0 0 1 1-.25 11.4 11.4 0 0 0 3.6.57 1 1 0 0 1 1 1V20a1 1 0 0 1-1 1A17 17 0 0 1 3 4a1 1 0 0 1 1-1h3.5a1 1 0 0 1 1 1c0 1.25.2 2.45.57 3.57a1 1 0 0 1-.25 1z"/></svg>
          1300 555 210
        </li>
        <li class="contact__item">
          <svg class="contact__icon" viewBox="0 0 24 24" aria-hidden="true"><path fill="var(--amber)" d="M6.6 10.8a15.1 15.1 0 0 0 6.6 6.6l2.2-2.2a1 1 0 0 1 1-.25 11.4 11.4 0 0 0 3.6.57 1 1 0 0 1 1 1V20a1 1 0 0 1-1 1A17 17 0 0 1 3 4a1 1 0 0 1 1-1h3.5a1 1 0 0 1 1 1c0 1.25.2 2.45.57 3.57a1 1 0 0 1-.25 1z"/></svg>
          +61 3 5550 1234
        </li>
        <li class="contact__item">
          <svg class="contact__icon" viewBox="0 0 24 24" aria-hidden="true"><rect x="2" y="5" width="20" height="14" rx="1.5" fill="var(--amber)"/><path d="M3 6.5l9 6.5 9-6.5" fill="none" stroke="#fff" stroke-width="1.6"/></svg>
          info@homewardhaven.org
        </li>
        <li class="contact__item">
          <svg class="contact__icon" viewBox="0 0 24 24" aria-hidden="true"><g fill="none" stroke="var(--amber)" stroke-width="1.8"><circle cx="12" cy="12" r="9.5"/><ellipse cx="12" cy="12" rx="4" ry="9.5"/><path d="M2.5 12h19M4.5 7h15M4.5 17h15"/></g></svg>
          www.homewardhaven.org
        </li>
      </ul>
    </div>
  </section>

</main>
</body>
</html>
```